Business Card for Jewelry Business

We need a new namecard design for a jewelry company based in Bangkok, Thailand. We have a new website recently and want the new namecard to reflect our new modern image. I have uploaded our old namecard to show you the information that needs to be on the namecard. Pls check our website www.qelnotrax.com for the new color scheme to help design the new namecard.

```html
<!DOCTYPE html>
<html lang="en">
<head>
<meta charset="utf-8">
<title>Qelnotrax Jewelers – Business Card</title>
<link rel="stylesheet" href="https://fonts.googleapis.com/css2?family=Libre+Baskerville:ital,wght@0,400;1,700&family=Poppins:wght@400;500&display=swap">
<style>
  :root {
    --backdrop: #2b2b30;
    --teal: #52c3cb;
    --teal-deep: #3fb0b9;
    --paper: #ffffff;
    --navy: #1c1f3b;
    --ink: #585a60;
    --ink-soft: #8c8f96;
  }
  * { margin: 0; padding: 0; box-sizing: border-box; }
  html, body { width: 1200px; height: 801px; overflow: hidden; }
  body {
    background: var(--backdrop);
    font-family: "Poppins", sans-serif;
    position: relative;
  }
  .card {
    position: absolute;
    top: 246px;
    width: 540px;
    height: 309px;
    border-radius: 2px;
    box-shadow: 0 18px 40px rgba(0,0,0,.45);
    overflow: hidden;
  }
  .card--front { left: 45px; background: var(--teal); }
  .card--back { left: 615px; background: var(--paper); }

  .wordmark {
    font-family: "Libre Baskerville", serif;
    font-weight: 400;
    color: var(--navy);
    display: flex;
    align-items: center;
    gap: 10px;
  }
  .wordmark__dot {
    width: 14px; height: 14px; border-radius: 50%;
    background: var(--paper);
  }
  .card--back .wordmark__dot { background: var(--teal); }
  .wordmark__name { font-size: 28px; letter-spacing: 1px; line-height: 1; }
  .wordmark__sub { font-size: 9px; letter-spacing: 1.2px; text-align: right; margin-top: 4px; }

  .card--front .brand {
    position: absolute; left: 50%; top: 96px; transform: translateX(-50%);
  }
  .website {
    position: absolute; left: 0; right: 0; top: 210px;
    text-align: center;
    font-size: 13px; letter-spacing: 6px;
    color: var(--navy);
  }

  .card--back .brand { position: absolute; right: 34px; top: 34px; }
  .person { position: absolute; left: 34px; top: 140px; }
  .person__name {
    font-family: "Libre Baskerville", serif;
    font-style: italic; font-weight: 700;
    font-size: 19px; color: var(--navy); letter-spacing: .5px;
  }
  .person__role {
    font-family: "Libre Baskerville", serif;
    font-size: 10px; color: var(--teal); letter-spacing: .6px;
    margin-top: 3px;
  }
  .address {
    font-size: 9.5px; color: var(--ink); line-height: 1.45; margin-top: 9px;
  }
  .contacts { list-style: none; margin-top: 10px; }
  .contacts li {
    display: flex; align-items: center; gap: 6px;
    font-size: 10px; color: var(--ink); line-height: 1; margin-bottom: 6px;
  }
  .icon { width: 14px; height: 14px; flex: none; }
  .sep { color: var(--ink-soft); margin: 0 3px; }
</style>
</head>
<body>

<section class="card card--front" aria-label="Card front">
  <div class="brand wordmark">
    <span class="wordmark__dot"></span>
    <div>
      <div class="wordmark__name">QELNOTRAX</div>
      <div class="wordmark__sub">JEWELERS</div>
    </div>
  </div>
  <p class="website">www.qelnotrax.com</p>
</section>

<section class="card card--back" aria-label="Card back">
  <div class="brand wordmark">
    <span class="wordmark__dot"></span>
    <div>
      <div class="wordmark__name">QELNOTRAX</div>
      <div class="wordmark__sub">JEWELERS</div>
    </div>
  </div>

  <div class="person">
    <h1 class="person__name">NARA PIMCHAN</h1>
    <p class="person__role">SALES &amp; PRODUCT DEVELOPMENT MANAGER</p>
    <p class="address">88 Moo 2, Sukprasert road, Trade Zone 5<br>Bang Wua Industrial Park, Bang Wua, Bangkok, 10990 Thailand</p>
    <ul class="contacts">
      <li>
        <svg class="icon" viewBox="0 0 14 14"><circle cx="7" cy="7" r="7" fill="var(--teal)"/><path d="M4.6 3.8l1.3 1.5-.7.8c.5 1 1.2 1.7 2.2 2.2l.8-.7 1.5 1.3-.8 1c-2.5-.3-4.9-2.7-5.2-5.2z" fill="#fff"/></svg>
        +662 - 418 - 2270 - 3<span class="sep">|</span>
        <svg class="icon" viewBox="0 0 14 14"><circle cx="7" cy="7" r="7" fill="var(--teal)"/><rect x="4" y="6" width="6" height="3.5" rx=".5" fill="#fff"/><rect x="5" y="3.8" width="4" height="2" fill="#fff"/><rect x="5" y="8.5" width="4" height="1.8" fill="var(--teal)" stroke="#fff" stroke-width=".6"/></svg>
        +662 - 418 - 5521
      </li>
      <li>
        <svg class="icon" viewBox="0 0 14 14"><circle cx="7" cy="7" r="7" fill="var(--teal)"/><rect x="3.6" y="4.6" width="6.8" height="4.8" fill="none" stroke="#fff" stroke-width=".9"/><path d="M3.6 4.6L7 7.4l3.4-2.8" fill="none" stroke="#fff" stroke-width=".9"/></svg>
        nara@qelnotrax.com , hello@qelnotrax.com
      </li>
      <li>
        <svg class="icon" viewBox="0 0 14 14"><circle cx="7" cy="7" r="7" fill="var(--teal)"/></svg>
        Qelnotrax Jewelers<span class="sep">|</span>
        <svg class="icon" viewBox="0 0 14 14"><circle cx="7" cy="7" r="7" fill="var(--teal)"/></svg>
        @QelnotraxCo
      </li>
    </ul>
  </div>
</section>

</body>
</html>
```